T&K Holdings

Design a modern simple business card. I have attached a clean version of a card we like form Harbor Pines another company we own. I also attached the old T&K card design and logo and a couple of ideas we had but just can't finalize on whether we like them or not. We would like to include the 20 year logo somewhere on the card.

```html
<!DOCTYPE html>
<html lang="en">
<head>
<meta charset="utf-8">
<title>T&amp;K Holdings – Business Card</title>
<link href="https://fonts.googleapis.com/css2?family=Poppins:wght@400;500;700&display=swap" rel="stylesheet">
<style>
  :root {
    --navy: #25226b;
    --navy-deep: #201d62;
    --grey: #7f7f7f;
    --grey-light: #9a9a9a;
    --white: #ffffff;
    --stage: #3a3a3a;
  }
  * { box-sizing: border-box; margin: 0; padding: 0; }
  html, body { width: 1200px; height: 689px; overflow: hidden; }
  body {
    background: var(--stage);
    font-family: "Poppins", sans-serif;
    position: relative;
  }
  .card {
    position: absolute;
    top: 190px;
    width: 540px;
    height: 309px;
    border-radius: 18px;
    overflow: hidden;
  }

  /* Back side */
  .card--back { left: 40px; background: var(--navy); color: var(--white); }
  .anniversary {
    position: absolute; left: 34px; top: 58px; width: 150px;
    text-align: center; color: var(--white); font-weight: 500;
  }
  .anniversary__number { font-size: 58px; line-height: 1; }
  .anniversary__label { font-size: 13px; letter-spacing: 3px; margin-top: 4px; }
  .anniversary__years { font-size: 13px; letter-spacing: 1px; }
  .back__divider {
    position: absolute; left: 44px; top: 170px; width: 130px; height: 1px;
    background: rgba(255,255,255,0.6);
  }
  .back__brand {
    position: absolute; left: 34px; top: 188px; width: 150px;
    text-align: center; font-size: 44px; font-weight: 700; color: var(--white);
  }
  .services { position: absolute; left: 236px; top: 70px; }
  .services__title {
    font-size: 17px; font-weight: 700; line-height: 1.2; text-transform: uppercase;
    letter-spacing: 0.5px; margin-bottom: 18px;
  }
  .services__list { list-style: none; }
  .services__list li {
    font-size: 15px; font-weight: 500; line-height: 1.75;
    position: relative; padding-left: 20px;
  }
  .services__list li::before {
    content: ""; position: absolute; left: 0; top: 11px;
    width: 7px; height: 7px; border-radius: 50%; background: var(--grey-light);
  }

  /* Front side */
  .card--front { left: 620px; background: var(--white); }
  .front__brand {
    position: absolute; left: 38px; top: 96px; width: 180px;
    text-align: center; font-size: 62px; font-weight: 700; color: var(--navy);
  }
  .front__divider {
    position: absolute; left: 236px; top: 48px; width: 1px; height: 180px;
    background: #c9c9c9;
  }
  .contact { position: absolute; left: 258px; top: 58px; color: var(--grey); }
  .contact__name { font-size: 19px; font-weight: 700; color: var(--navy); line-height: 1.1; }
  .contact__role { font-size: 12px; margin-bottom: 14px; }
  .contact__line {
    display: flex; align-items: center; gap: 7px;
    font-size: 12.5px; line-height: 1.6;
  }
  .contact__line svg { width: 12px; height: 12px; fill: var(--navy); flex: none; }
  .contact__address { font-size: 12.5px; line-height: 1.45; margin-top: 12px; }
  .front__band { position: absolute; left: 0; bottom: 0; width: 100%; height: 44px; }
  .front__band-mark {
    position: absolute; right: 22px; bottom: 8px;
    font-size: 18px; font-weight: 700; color: var(--navy);
  }
</style>
</head>
<body>

<section class="card card--back" aria-label="Business card back">
  <div class="anniversary">
    <div class="anniversary__number">20</div>
    <div class="anniversary__label">YEARS</div>
    <div class="anniversary__years">2004-2024</div>
  </div>
  <div class="back__divider"></div>
  <div class="back__brand">T&amp;K</div>

  <div class="services">
    <h2 class="services__title">Integrated<br>Industrial Services</h2>
    <ul class="services__list">
      <li>Mechanical / Civil</li>
      <li>I&amp;E</li>
      <li>Fabrication</li>
      <li>Rotating</li>
      <li>Heat Transfer Equipment</li>
    </ul>
  </div>
</section>

<section class="card card--front" aria-label="Business card front">
  <div class="front__brand">T&amp;K</div>
  <div class="front__divider"></div>

  <div class="contact">
    <div class="contact__name">DANA WHITFIELD</div>
    <div class="contact__role">IT Director</div>
    <div class="contact__line">
      <svg viewBox="0 0 24 24"><path d="M6.6 10.8a15.1 15.1 0 0 0 6.6 6.6l2.2-2.2a1 1 0 0 1 1-.25 11.4 11.4 0 0 0 3.6.57 1 1 0 0 1 1 1V20a1 1 0 0 1-1 1A17 17 0 0 1 3 4a1 1 0 0 1 1-1h3.5a1 1 0 0 1 1 1c0 1.25.2 2.45.57 3.57a1 1 0 0 1-.25 1z"/></svg>
      409-555-0148
    </div>
    <div class="contact__line">
      <svg viewBox="0 0 24 24"><path d="M6.6 10.8a15.1 15.1 0 0 0 6.6 6.6l2.2-2.2a1 1 0 0 1 1-.25 11.4 11.4 0 0 0 3.6.57 1 1 0 0 1 1 1V20a1 1 0 0 1-1 1A17 17 0 0 1 3 4a1 1 0 0 1 1-1h3.5a1 1 0 0 1 1 1c0 1.25.2 2.45.57 3.57a1 1 0 0 1-.25 1z"/></svg>
      409-555-0192
    </div>
    <div class="contact__line">
      <svg viewBox="0 0 24 24"><path d="M2 5h20v14H2z M2 5l10 8 10-8" fill="var(--navy)" stroke="#fff" stroke-width="1.5"/></svg>
      dwhitfield@tkhold.com
    </div>
    <div class="contact__address">418 Cedar Avenue, Suite 20<br>Port Arlen, TX 77710</div>
  </div>

  <svg class="front__band" viewBox="0 0 540 44" preserveAspectRatio="none" aria-hidden="true">
    <rect x="0" y="14" width="540" height="30" fill="var(--navy)"/>
    <polygon points="440,44 470,0 540,0 540,44" fill="var(--grey)"/>
    <polygon points="420,44 450,14 470,14 440,44" fill="var(--white)"/>
  </svg>
  <div class="front__band-mark">T&amp;K</div>
</section>

</body>
</html>
```